Jewelry store needs fully functional Ecommerce website

Web Design Brief for our E-commerce Jewelry retail store.
Description

We need a fully coded Shopify website. The Shopify site will need to be fully functional with an Ecommerce integration (fully integrated with Paywise and All other gateways) and will need to be SEO optimized.
We sell jewelry items like: rings, earrings, necklaces etc. The website should have an elegant, modern, professional, fun, look.

***We would like the website to look and function similarly to this website:
https://velvorisco.com

Color Preference
Colors to be used are white background with black font and light pink/ purple/ gold tints. We have attached our logo as reference.

Functionalities
The store will function like a typical Ecommerce jewelry store, using the products/categories as the starting page. Going into individual product pages by selecting images and leading to a detailed “buy now” page for the selected product.

Target Market
Jewelry lovers.

Should Not Have:
- - Dull and common design
- - Messy/unstructured navigation

Coded - Design and coding required
Target Audience are women from 16-50 years old.
We will need to be able to add products and make modifications to the website as needed.

We need the following apps installed and Operating:
-Tally Shift; Order Look Up (rename “track your order”) ; Help Center (Questions and Answers) ; Pemmo Reviews; TXT Nudge; Drenoza Email Marketing ; Plivet (Pals messenger bump) ; Vantro multi- currency (translate currency to buyer) ; Discounted Upsell ; Easy Contact form App
We will need all products imported: (below is information for importing products). We will provide all links that serve entire active item product catalog in shopifys import format:
DataFeed:

If you are getting started with Shopify, a combination of the Shopify Import Format and XML feeds is ideal. The Shopify Import Format will output a file that can be uploaded into Shopify’s product database. After you import, you can use the XML feed and a third party app to keep the inventory up to date in real time, take down items that go out of stock etc., all without regular human intervention. There a several Shopify apps that can do this type of feed integration. We have had a good experience with Tally Shift, which is an app that can be configured to accept our XML feed and update products on a set schedule. You can even set your own margins based on our wholesale price with this app.

Shopify Formatted HTML TableTo make it easier to get started on Shopify, we included a format that outputs the required fields for a product import in Shopify. In order to use the embedded Excel file, first open the file (Auto-Shopify-Datasheet-Format.xslx), Refresh it (under Data tab), and then Save As with a new file name in a CSV (UTF-8) file. That file can then be split into smaller CSV files (if there is a limit on the number of products per file) for import into Shopify.

Target Market(s)

Jewelry Lovers

Industry/Entity Type

Jewelry Store

Coding

Number of Pages Required

5+ page

Colors
eda3c7
d3a5cc
ffffff

Requirements
Must have
• Color Preference
Colors to be used are white background with black font and light pink/ purple/ gold tints.

https://velvorisco.com
Should not have
• Should Not Have:

```html
<!DOCTYPE html>
<html lang="en">
<head>
<meta charset="utf-8">
<title>Shop – Jewelry Store</title>
<link href="https://fonts.googleapis.com/css2?family=Playfair+Display:wght@400;700&family=Poppins:wght@300;400;500;600&display=swap" rel="stylesheet">
<style>
:root{
  --ink:#1f1f1f;
  --text:#333;
  --muted:#777;
  --line:#dcdcdc;
  --dark:#2b2b2b;
  --pink:#eda3c7;
  --lilac:#d3a5cc;
  --band:#d4a3cf;
  --rose:#d19a82;
  --silver:#a9adb8;
  --gold:#c9a743;
  --white:#fff;
}
*{box-sizing:border-box;margin:0;padding:0}
html,body{width:1200px;height:2857px;overflow:hidden;background:var(--white)}
body{font-family:'Poppins',sans-serif;color:var(--text);position:relative}
.serif{font-family:'Playfair Display',serif}
.abs{position:absolute}
a{color:inherit;text-decoration:none}

.topbar{position:absolute;left:0;top:0;width:1200px;height:27px;background:var(--dark);color:#fff;font-size:11.5px;font-weight:600;letter-spacing:1px;text-align:center;line-height:27px}
.nav{position:absolute;left:0;top:27px;width:1200px;height:68px}
.nav-links{position:absolute;left:88px;top:27px;display:flex;gap:32px;font-size:12px;font-weight:500;letter-spacing:1px;color:var(--ink)}
.logo{position:absolute;left:0;width:1200px;top:20px;text-align:center;font-family:'Playfair Display',serif;font-size:22px;color:var(--ink);letter-spacing:.5px}
.nav-icons{position:absolute;right:96px;top:22px;display:flex;gap:30px}
.nav-icons svg{width:24px;height:24px;stroke:#444;fill:none;stroke-width:1.4}
.cart-badge{position:absolute;right:96px;top:43px;width:10px;height:10px;border-radius:50%;background:var(--pink);color:#fff;font-size:6px;text-align:center;line-height:10px}

.hero{position:absolute;left:0;top:95px;width:1200px;height:195px;background:linear-gradient(90deg,#fbe9ee 0%,#f7d3df 45%,#f1bfd0 70%,#f6dbe3 100%)}
.hero-photo{position:absolute;left:560px;top:0;width:640px;height:195px;background:radial-gradient(ellipse at 50% 70%,rgba(222,170,110,.55),rgba(240,190,205,0) 65%)}
.hero h1{position:absolute;left:88px;top:70px;font-family:'Playfair Display',serif;font-weight:400;font-size:46px;color:var(--ink)}

.sidebar{position:absolute;left:88px;top:375px;width:216px}
.cat-head{height:48px;background:var(--dark);color:#fff;display:flex;align-items:center;padding-left:24px;font-size:15px;font-weight:600;letter-spacing:.5px;gap:10px}
.cat-head .chev{margin-left:auto;margin-right:18px;font-size:11px}
.cat-list{margin-top:16px;font-size:13px;color:#555}
.cat-list li{list-style:none;height:27px;display:flex;justify-content:space-between;align-items:center}
.view-all{display:inline-block;margin-top:14px;color:var(--pink);font-weight:600;font-size:13px;letter-spacing:.5px;border-bottom:1px solid var(--pink)}
.filter{height:49px;border-bottom:2px solid var(--line);display:flex;justify-content:space-between;align-items:flex-end;padding-bottom:6px;font-size:13px;font-weight:600;color:var(--ink);letter-spacing:.3px}
.price-range{position:relative;height:48px}
.price-range .lbls{display:flex;justify-content:space-between;font-size:10px;color:#666;margin-top:8px}
.price-range .track{position:absolute;left:10px;right:8px;top:34px;height:3px;background:var(--ink)}
.price-range .knob{position:absolute;top:27px;width:17px;height:17px;border-radius:50%;background:#fff;border:4px solid var(--ink)}
.sortby h4{font-size:13px;font-weight:600;color:var(--ink);margin:30px 0 8px}
.sortby li{list-style:none;height:27px;display:flex;align-items:center;gap:7px;font-size:12px;color:#444}
.sortby li i{width:11px;height:11px;border:1.5px solid #333;border-radius:2px}

.toolbar{position:absolute;left:355px;top:383px;width:756px;height:32px;font-size:13px;font-weight:600;color:var(--ink)}
.toolbar .count{position:absolute;left:0;top:10px}
.toolbar .sort{position:absolute;left:335px;top:10px}
.select{position:absolute;top:0;height:30px;border:1px solid #ccc;font-weight:400;color:#777;font-size:13px;padding:5px 10px;display:flex;justify-content:space-between}
.select b{color:#333;font-size:10px;margin-top:3px}

.grid{position:absolute;left:355px;top:452px;width:756px;display:grid;grid-template-columns:243px 243px 243px;column-gap:14px;row-gap:18px}
.card{height:330px;background:#fff;box-shadow:0 6px 22px rgba(0,0,0,.08);text-align:center}
.card .photo{height:190px;margin:0 10px}
.card h3{font-family:'Playfair Display',serif;font-weight:700;font-size:15.5px;line-height:22px;color:#3a3a3a;margin-top:5px;letter-spacing:.3px}
.card .price{font-size:19px;color:#777;margin-top:6px;letter-spacing:.5px}
.swatches{display:flex;justify-content:center;gap:10px;margin-top:16px}
.swatches span{width:17px;height:17px;border-radius:50%}
.s1{background:var(--rose)}.s2{background:var(--silver)}.s3{background:var(--gold)}

.pager{position:absolute;top:1889px;left:520px;display:flex;align-items:center;font-size:17px;color:#333}
.pager .btn{height:38px;padding:0 24px;line-height:38px;font-size:14px;background:#eee}
.pager .next{background:var(--pink);color:#fff;font-weight:500}
.pager .num{margin-left:28px}
.pager .cur{width:47px;height:47px;border-radius:50%;background:var(--dark);color:#fff;text-align:center;line-height:47px;margin-left:26px}

.features{position:absolute;top:2024px;left:160px;width:880px;display:flex;justify-content:space-between}
.feature{width:200px;text-align:center;font-size:14.5px;color:#666;line-height:20px}
.feature svg{width:56px;height:60px;stroke:var(--lilac);fill:none;stroke-width:2;margin-bottom:10px}

.newsletter{position:absolute;left:0;top:2238px;width:1200px;height:223px;background:var(--band);color:#fff}
.newsletter h2{position:absolute;left:88px;top:44px;font-family:'Playfair Display',serif;font-weight:400;font-size:40px;line-height:40px;letter-spacing:1px}
.newsletter p{position:absolute;left:88px;top:146px;width:470px;font-size:15.5px;line-height:20px;color:#fbeef8}
.subscribe{position:absolute;left:632px;top:83px;width:478px;height:58px;background:#fff;display:flex;align-items:center;padding:5px}
.subscribe .field{flex:1;display:flex;align-items:center;gap:10px;padding-left:15px;color:#888;font-size:14.5px}
.subscribe .field svg{width:17px;height:13px;fill:#8a95a6}
.subscribe .go{height:48px;width:119px;background:var(--pink);color:#fff;font-weight:600;font-size:13px;letter-spacing:.5px;text-align:center;line-height:48px}

.footer-col{position:absolute;top:2536px}
.footer-col h4{font-family:'Playfair Display',serif;font-weight:400;font-size:19px;color:var(--ink);letter-spacing:.3px;margin-bottom:18px}
.footer-col li{list-style:none;font-size:13px;color:#444;height:26.6px}
.contact-item{display:flex;gap:10px;font-size:13px;color:#444;line-height:18px;margin-bottom:9px}
.contact-item svg{width:13px;height:13px;fill:var(--pink);flex:none;margin-top:2px}
.socials{display:flex;gap:8px;margin-bottom:34px}
.socials span{display:flex;align-items:center;gap:4px;font-size:11px;color:#444}
.socials i{width:14px;height:14px;border-radius:50%;background:var(--lilac)}
.pay{display:flex;gap:8px}
.pay span{width:50px;height:32px;border:1px solid #ddd;border-radius:4px;font-size:10px;font-weight:500;color:#333;text-align:center;line-height:30px}
.rule{position:absolute;left:91px;top:2797px;width:1020px;height:1px;background:#ccc}
.copy{position:absolute;left:0;width:1200px;top:2818px;text-align:center;font-size:13px;font-weight:500;color:#333;letter-spacing:.3px}
.to-top{position:absolute;left:1133px;top:2768px;width:40px;height:40px;border-radius:50%;background:var(--pink)}
.to-top svg{width:40px;height:40px;stroke:#fff;stroke-width:1.5;fill:none}
</style>
</head>
<body>

<div class="topbar">FREE US SHIPPING ON ORDERS $50+</div>

<header class="nav">
  <nav class="nav-links"><a>HOME</a><a>SHOP</a><a>PRODUCT</a></nav>
  <div class="logo">LOGO HERE</div>
  <div class="nav-icons">
    <svg viewBox="0 0 24 24"><circle cx="10.5" cy="10.5" r="7.5"/><path d="M16 16l6 6"/></svg>
    <svg viewBox="0 0 24 24"><circle cx="12" cy="8" r="5"/><path d="M3 22c1-5 5-7 9-7s8 2 9 7"/></svg>
    <svg viewBox="0 0 24 24"><path d="M12 21s-9-6-9-12a5 5 0 0 1 9-3 5 5 0 0 1 9 3c0 6-9 12-9 12z"/></svg>
    <svg viewBox="0 0 24 24"><path d="M4 8h16l-1 14H5z"/><path d="M8 8V6a4 4 0 0 1 8 0v2"/></svg>
  </div>
  <div class="cart-badge">0</div>
</header>

<section class="hero">
  <div class="hero-photo" role="img" aria-label="Two gold rings with diamonds on soft pink petals"></div>
  <h1>SHOP</h1>
</section>

<aside class="sidebar">
  <div class="cat-head">
    <svg width="18" height="14" viewBox="0 0 18 14" stroke="#fff" stroke-width="1.5"><path d="M5 2h13M0 7h18M5 12h13"/></svg>
    CATEGORIES <span class="chev">&#8964;</span>
  </div>
  <ul class="cat-list">
    <li>Ring <span>&rsaquo;</span></li>
    <li>Bracelet <span>&rsaquo;</span></li>
    <li>Earrings <span>&rsaquo;</span></li>
    <li>Necklace <span>&rsaquo;</span></li>
  </ul>
  <a class="view-all">VIEW ALL</a>
  <div class="filter" style="height:53px">COLOR <span>&rsaquo;</span></div>
  <div class="filter">JEWELRY <span>&rsaquo;</span></div>
  <div class="filter" style="border-bottom:none">PRICE <span>&#8964;</span></div>
  <div class="price-range">
    <div class="lbls"><span>$0.00</span><span>$10000.00</span></div>
    <div class="track"></div>
    <div class="knob" style="left:1px"></div>
    <div class="knob" style="right:-1px"></div>
  </div>
  <div class="filter">MATERIAL <span>&rsaquo;</span></div>
  <div class="filter">RING SIZE <span>&rsaquo;</span></div>
  <div class="filter">RATING <span>&rsaquo;</span></div>
  <div class="filter">AVAILABILITY <span>&rsaquo;</span></div>
  <div class="sortby">
    <h4>SORT BY:</h4>
    <ul>
      <li><i></i>NONE</li>
      <li><i></i>FEATURED</li>
      <li><i></i>BEST SELLERS</li>
      <li><i></i>PRICE: LOW - HIGH</li>
      <li><i></i>PRICE: HIGH - LOW</li>
      <li><i></i>NEWEST FIRST</li>
    </ul>
  </div>
</aside>

<div class="toolbar">
  <span class="count">SHOWING 1 – 60 OF 173 RESULTS</span>
  <span class="sort">Sort by:</span>
  <div class="select" style="left:393px;width:113px">Bestselling <b>&#8964;</b></div>
  <span class="sort" style="left:545px">Items per page:</span>
  <div class="select" style="left:664px;width:92px">60 <b>&#8964;</b></div>
</div>

<main class="grid">
  <article class="card"><div class="photo" role="img" aria-label="Silver jhumka earrings" style="background:radial-gradient(circle,#c9c9cc 0%,#fff 70%)"></div><h3>SOME OUR PRODUCT<br>HEADING GOES</h3><div class="price">$99.00</div><div class="swatches"><span class="s1"></span><span class="s2"></span><span class="s3"></span></div></article>
  <article class="card"><div class="photo" role="img" aria-label="Diamond solitaire ring" style="background:radial-gradient(circle,#d5d6d9 0%,#fff 70%)"></div><h3>SOME OUR PRODUCT<br>HEADING GOES</h3><div class="price">$99.00</div><div class="swatches"><span class="s1"></span><span class="s2"></span><span class="s3"></span></div></article>
  <article class="card"><div class="photo" role="img" aria-label="Silver chain bracelet" style="background:radial-gradient(circle,#c4c5c8 0%,#fff 70%)"></div><h3>SOME OUR PRODUCT<br>HEADING GOES</h3><div class="price">$99.00</div><div class="swatches"><span class="s1"></span><span class="s2"></span><span class="s3"></span></div></article>
  <article class="card"><div class="photo" role="img" aria-label="Rose gold flower bangle" style="background:radial-gradient(circle,#e6c7b2 0%,#fff 70%)"></div><h3>SOME OUR PRODUCT<br>HEADING GOES</h3><div class="price">$99.00</div><div class="swatches"><span class="s1"></span><span class="s2"></span><span class="s3"></span></div></article>
  <article class="card"><div class="photo" role="img" aria-label="Rose gold gemstone ring" style="background:radial-gradient(circle,#e8c2ad 0%,#fff 70%)"></div><h3>SOME OUR PRODUCT<br>HEADING GOES</h3><div class="price">$99.00</div><div class="swatches"><span class="s1"></span><span class="s2"></span><span class="s3"></span></div></article>
  <article class="card"><div class="photo" role="img" aria-label="Stack of mixed metal rings" style="background:radial-gradient(circle,#cfc8c0 0%,#fff 70%)"></div><h3>SOME OUR PRODUCT<br>HEADING GOES</h3><div class="price">$99.00</div><div class="swatches"><span class="s1"></span><span class="s2"></span><span class="s3"></span></div></article>
  <article class="card"><div class="photo" role="img" aria-label="Gold ring with amethyst" style="background:radial-gradient(circle,#e5cf8a 0%,#fff 70%)"></div><h3>SOME OUR PRODUCT<br>HEADING GOES</h3><div class="price">$99.00</div><div class="swatches"><span class="s1"></span><span class="s2"></span><span class="s3"></span></div></article>
  <article class="card"><div class="photo" role="img" aria-label="Gold pendant necklace" style="background:radial-gradient(circle,#ecd7bf 0%,#fff 60%)"></div><h3>SOME OUR PRODUCT<br>HEADING GOES</h3><div class="price">$99.00</div><div class="swatches"><span class="s1"></span><span class="s2"></span><span class="s3"></span></div></article>
  <article class="card"><div class="photo" role="img" aria-label="Engraved gold cuff bracelet" style="background:radial-gradient(circle,#e2c08e 0%,#fff 70%)"></div><h3>SOME OUR PRODUCT<br>HEADING GOES</h3><div class="price">$99.00</div><div class="swatches"><span class="s1"></span><span class="s2"></span><span class="s3"></span></div></article>
  <article class="card"><div class="photo" role="img" aria-label="Rose gold pearl pendant" style="background:radial-gradient(circle,#efd7cb 0%,#fff 60%)"></div><h3>SOME OUR PRODUCT<br>HEADING GOES</h3><div class="price">$99.00</div><div class="swatches"><span class="s1"></span><span class="s2"></span><span class="s3"></span></div></article>
  <article class="card"><div class="photo" role="img" aria-label="Crystal stud earrings" style="background:radial-gradient(circle,#cfd0d3 0%,#fff 70%)"></div><h3>SOME OUR PRODUCT<br>HEADING GOES</h3><div class="price">$99.00</div><div class="swatches"><span class="s1"></span><span class="s2"></span><span class="s3"></span></div></article>
  <article class="card"><div class="photo" role="img" aria-label="Crystal drop earrings" style="background:radial-gradient(circle,#d6d6d8 0%,#fff 65%)"></div><h3>SOME OUR PRODUCT<br>HEADING GOES</h3><div class="price">$99.00</div><div class="swatches"><span class="s1"></span><span class="s2"></span><span class="s3"></span></div></article>
</main>

<nav class="pager">
  <span class="btn">&lsaquo; Prev</span>
  <span class="num" style="margin-left:28px">1</span>
  <span class="cur">2</span>
  <span class="num" style="margin-left:26px">3</span>
  <span class="num" style="margin-left:22px;font-size:14px">...</span>
  <span class="num" style="margin-left:20px">82</span>
  <span class="btn next" style="margin-left:28px">Next &rsaquo;</span>
</nav>

<section class="features">
  <div class="feature"><svg viewBox="0 0 56 60"><path d="M4 22h30v24H4zM34 30h10l8 8v8H34"/><circle cx="14" cy="48" r="4"/><circle cx="44" cy="48" r="4"/><path d="M0 28h10M2 34h10M4 40h10"/></svg><div>Free US Shipping On<br>Orders Over $50</div></div>
  <div class="feature"><svg viewBox="0 0 56 60"><path d="M12 24l16-8 16 8v20l-16 8-16-8z"/><path d="M12 24l16 8 16-8M28 32v20"/><path d="M18 10h20a8 8 0 0 1 0 16"/></svg><div>Hassle-Free Returns Easily<br>Exchange Or Return Items</div></div>
  <div class="feature"><svg viewBox="0 0 56 60"><path d="M14 20h8l6-12c4 0 5 3 4 7l-1 5h10c3 0 4 3 3 5l-3 10H14z"/><path d="M10 48l3-6 3 6-6-4h6zM25 50l3-6 3 6-6-4h6zM40 48l3-6 3 6-6-4h6z"/></svg><div>Over 1 Million Followers<br>&amp; 11,000 5-Star Reviews</div></div>
  <div class="feature"><svg viewBox="0 0 56 60"><path d="M16 6c0 18 4 26 12 26s12-8 12-26"/><circle cx="28" cy="44" r="10"/><circle cx="28" cy="44" r="4"/></svg><div>Authentic women<br>Jewlry</div></div>
</section>

<section class="newsletter">
  <h2>SUBSCRIBE<br>NEWSLETTER</h2>
  <p>By subscribing to our mailing list you will always be updated with the latest news from us.</p>
  <form class="subscribe">
    <div class="field"><svg viewBox="0 0 17 13"><path d="M0 0h17v13H0z M1 1l7.5 6L16 1"/></svg>Enter your email address</div>
    <div class="go">SIGN ME UP!</div>
  </form>
</section>

<div class="footer-col" style="left:127px">
  <h4>LET US HELP YOU</h4>
  <ul><li>Search</li><li>About Us</li><li>Ring Size Guide</li><li>Jewelry Care Guide</li><li>Shipping</li><li>Contact</li><li>FAQ'S</li></ul>
</div>
<div class="footer-col" style="left:364px">
  <h4>INFORMATION</h4>
  <ul><li>Site Map</li><li>Terms &amp; Condition</li><li>Privacy Policy</li><li>FAQ's</li><li>Customer Service</li><li>Disclamier</li></ul>
</div>
<div class="footer-col" style="left:588px">
  <h4>CONTACT US</h4>
  <div class="contact-item"><svg viewBox="0 0 13 13"><path d="M0 2h13v9H0z"/></svg><div>Email:<br>Info@example.com.au</div></div>
  <div class="contact-item"><svg viewBox="0 0 13 13"><path d="M2 0l3 3-1.5 2a8 8 0 0 0 4.5 4.5L10 8l3 3-2 2C5 13 0 8 0 2z"/></svg><div>Phone:<br>(+08) 123 456 7890</div></div>
  <div class="contact-item"><svg viewBox="0 0 13 13"><path d="M6.5 0a4.5 4.5 0 0 1 4.5 4.5C11 8 6.5 13 6.5 13S2 8 2 4.5A4.5 4.5 0 0 1 6.5 0zm0 3a1.5 1.5 0 1 0 0 3 1.5 1.5 0 0 0 0-3z"/></svg><div>Office Location:<br>Some address line goes here<br>city name</div></div>
</div>
<div class="footer-col" style="left:849px">
  <h4>STAY CONNECTED</h4>
  <div class="socials"><span><i></i>Pals</span><span><i></i>Chirp</span><span><i></i>Snapo</span></div>
  <h4>PAYMENT METHOD</h4>
  <div class="pay"><span>Paywise</span><span>Cardra</span><span>Mintcard</span><span>Novapay</span></div>
</div>

<div class="rule"></div>
<div class="copy">© COPYRIGHT 2021 - ALL RIGHTS RESERVED</div>
<div class="to-top"><svg viewBox="0 0 40 40"><path d="M20 27V13M14 19l6-6 6 6"/></svg></div>

</body>
</html>
```